4th Generation Family Business Needs a New Card Design!

We are a family owned 4th Generation company. We are based in the Sydney, Australia area and we are desperately in need of a more modern and classy card. We are monumental masons who design, supply & erect lasting memorials throughout cemeteries in Sydney. Our customers are normally in a period of grieving. I have attached logo files that will need to be implemented on the card. Company was established 1935. Australian Owned and Operated. Card needs to be designed to PRINTLY.com specification.

Target Market(s)

Our target market is based upon people that a grieving for family members that have passed away. We also deal with alot of companies that own and operate cemeteries.

Industry/Entity Type

Business

Contact Information for Business Card

Oliver Brantley, Operations Manager, 0417552908, oliver@hollowaystoneworks.com.au
Martin Brantley, Director, 0431906627, martin@hollowaystoneworks.com.au
Phone # 02 9634 2258
Website: www.hollowaystoneworks.com.au
Address: Suite 17, 8 Calloway Lane, East Penrose, Sydney NSW 2290

Font styles to use
Serif
Decorative
Script

Requirements
Must have
• Would like to see the logo nicely implemented with a modern design. Embossed lettering would be a nice additive.

```html
<!DOCTYPE html>
<html lang="en">
<head>
<meta charset="utf-8">
<title>Holloway Stoneworks – Business Card</title>
<link rel="stylesheet" href="https://fonts.googleapis.com/css2?family=Cinzel:wght@400;600&family=Tinos&display=swap">
<style>
  :root {
    --backdrop: #e4e4e4;
    --card-black: #0b0b0c;
    --card-black-soft: #1c1c1e;
    --card-white: #f7f7f7;
    --gold: #d4aa2a;
    --ink: #1a1a1a;
    --ink-soft: #3a3a3a;
    --rule: #d2d2d2;
  }
  * { box-sizing: border-box; margin: 0; padding: 0; }
  html, body { width: 1200px; height: 576px; overflow: hidden; }
  body {
    background: var(--backdrop);
    position: relative;
    font-family: "Tinos", "Times New Roman", serif;
  }
  .card {
    position: absolute;
    top: 138px;
    width: 485px;
    height: 294px;
    overflow: hidden;
    box-shadow: 0 2px 6px rgba(0,0,0,0.25);
  }
  /* Front */
  .card-front {
    left: 81px;
    background: linear-gradient(100deg, var(--card-black) 0%, var(--card-black-soft) 30%, var(--card-black) 55%, var(--card-black) 100%);
  }
  .card-front .gold-strip {
    position: absolute; left: 0; right: 0; bottom: 0; height: 10px;
    background: var(--gold);
  }
  .wordmark {
    position: absolute;
    left: 0; right: 0;
    text-align: center;
    font-family: "Cinzel", "Times New Roman", serif;
    font-weight: 600;
    line-height: 1;
  }
  .card-front .wordmark { top: 96px; color: #ffffff; }
  .wordmark .word-main { display: block; font-size: 44px; letter-spacing: 1px; }
  .wordmark .word-sub { display: block; font-size: 21px; letter-spacing: 2px; margin-top: 8px; }
  .wordmark .mark-square {
    display: block; width: 14px; height: 14px; margin: 0 auto 14px;
    background: var(--gold);
  }

  /* Back */
  .card-back { left: 602px; background: var(--card-white); }
  .card-back .wordmark { left: 18px; right: auto; width: 180px; top: 98px; color: var(--ink); }
  .card-back .wordmark .word-main { font-size: 31px; }
  .card-back .wordmark .word-sub { font-size: 15px; margin-top: 6px; }
  .card-back .wordmark .mark-square { width: 11px; height: 11px; margin-bottom: 11px; }
  .divider {
    position: absolute; left: 210px; top: 62px; width: 1px; height: 144px;
    background: var(--rule);
  }
  .person { position: absolute; left: 239px; top: 64px; }
  .person-name {
    font-family: "Cinzel", "Times New Roman", serif;
    font-weight: 600; font-size: 20px; color: var(--ink); letter-spacing: 0.5px;
  }
  .person-role { font-size: 12px; color: var(--ink-soft); margin-top: 4px; }
  .contact-list { list-style: none; position: absolute; left: 239px; top: 116px; }
  .contact-list li {
    display: flex; align-items: center; gap: 9px;
    font-size: 13px; color: var(--ink-soft); height: 17.5px;
  }
  .contact-list svg { width: 10px; height: 10px; fill: var(--gold); flex: none; }
  .address {
    position: absolute; left: 239px; top: 172px;
    font-size: 13px; line-height: 19px; color: var(--ink-soft);
  }
  .footer-gold {
    position: absolute; left: 0; bottom: 4px; width: 215px; height: 18px;
    background: var(--gold);
  }
  .footer-black {
    position: absolute; right: 0; bottom: 0; width: 288px; height: 38px;
    background: var(--card-black);
    clip-path: polygon(22px 0, 100% 0, 100% 100%, 0 100%);
    color: #e8e8e8; font-size: 12.5px;
    padding: 12px 0 0 40px;
  }
</style>
</head>
<body>
  <section class="card card-front">
    <div class="wordmark">
      <span class="mark-square"></span>
      <span class="word-main">HOLLOWAY</span>
      <span class="word-sub">STONEWORKS</span>
    </div>
    <div class="gold-strip"></div>
  </section>

  <section class="card card-back">
    <div class="wordmark">
      <span class="mark-square"></span>
      <span class="word-main">HOLLOWAY</span>
      <span class="word-sub">STONEWORKS</span>
    </div>
    <div class="divider"></div>
    <div class="person">
      <div class="person-name">Oliver Brantley</div>
      <div class="person-role">Operations Manager</div>
    </div>
    <ul class="contact-list">
      <li>
        <svg viewBox="0 0 10 10"><path d="M2 0.5 L3.6 2.6 L2.7 3.6 Q3.6 5.7 6.3 7.3 L7.4 6.4 L9.5 8 L8.3 9.5 Q4 9 0.5 1.8 Z"/></svg>
        0431906627
      </li>
      <li>
        <svg viewBox="0 0 10 10"><path d="M0 3 Q5 0 10 3 L10 4.2 L7.5 4.2 L7.5 3.4 L2.5 3.4 L2.5 4.2 L0 4.2 Z M2 5 L8 5 L9 9.5 L1 9.5 Z"/></svg>
        02 9634 2258
      </li>
      <li>
        <svg viewBox="0 0 10 10"><path d="M0 2 L10 2 L10 3 L5 6 L0 3 Z M0 4 L5 7 L10 4 L10 8.5 L0 8.5 Z"/></svg>
        martin@hollowaystoneworks.com.au
      </li>
    </ul>
    <p class="address">Suite 17, 8 Calloway Lane,<br>East Penrose, Sydney NSW 2290</p>
    <div class="footer-gold"></div>
    <div class="footer-black">www.hollowaystoneworks.com.au</div>
  </section>
</body>
</html>
```